Homepage design for site providing cloud based engineering applications

I need the design for the homepage of a new site providing cloud based engineering applicaitons. The items that must have are provided in the attached pdf file. The layout and colors shown in the attached file is not intened to restrict your design. You should be creative to come up with your best design. We may have many applications. How to show these applicaitons on the homepage would be very important. Anyway, we want our hompage to be simple and clear.

Target Market(s)

Structure engineers(People design bridges, buildings and wharfs etc.)

Industry/Entity Type

Engineering

Requirements
Must have
• See attached pdf file.
Should not have
• No flash will be used.

```html
<!DOCTYPE html>
<html lang="en">
<head>
<meta charset="utf-8">
<title>Stratus Apps – Cloud Engineering Applications</title>
<link href="https://fonts.googleapis.com/css2?family=Ubuntu:wght@300;400;500&display=swap" rel="stylesheet">
<style>
  :root {
    --bg: #1d1d1d;
    --bg-deep: #0f0f0f;
    --header-top: #2b2b2b;
    --accent: #4ab2ee;
    --accent-dark: #1f8fd6;
    --client-red: #e63a1c;
    --text-light: #e4e4e4;
    --text-body: #3a3a3a;
    --panel: #ffffff;
    --strip: #000000;
    --footer: #0e0e0e;
    --muted: #8a8a8a;
  }
  * { margin: 0; padding: 0; box-sizing: border-box; }
  html, body { width: 1200px; height: 840px; overflow: hidden; }
  body {
    position: relative;
    background: radial-gradient(ellipse at 70% 40%, #262626 0%, var(--bg) 55%, #181818 100%);
    font-family: "Ubuntu", "Trebuchet MS", sans-serif;
    color: var(--text-light);
  }
  .abs { position: absolute; }

  /* Header */
  .site-header {
    position: absolute; left: 0; top: 0; width: 1200px; height: 61px;
    background: linear-gradient(var(--header-top), var(--bg-deep));
    border-bottom: 1px solid #333;
  }
  .brand { position: absolute; left: 120px; top: 14px; display: flex; align-items: center; gap: 14px; }
  .brand-dot { width: 34px; height: 34px; border-radius: 50%; border: 3px solid var(--accent); }
  .brand-name { font-size: 27px; font-weight: 300; color: #fff; letter-spacing: 0.2px; }
  .main-nav { position: absolute; right: 137px; top: 21px; display: flex; font-size: 14px; }
  .main-nav a { color: #fff; text-decoration: none; }
  .main-nav a.is-current { color: var(--accent); }
  .main-nav .sep { color: var(--muted); margin: 0 14px; font-size: 18px; line-height: 16px; }
  .header-rule { position: absolute; left: 121px; top: 62px; width: 968px; height: 4px; background: var(--accent); }
  .account-menu {
    position: absolute; left: 956px; top: 66px; width: 133px; height: 26px;
    background: #363636; border-radius: 0 0 3px 3px; font-size: 12px; color: #eee;
    padding: 6px 0 0 8px;
  }
  .account-menu svg { position: absolute; right: 8px; top: 9px; }

  /* Intro */
  .intro-title {
    position: absolute; left: 121px; top: 160px; font-size: 56px; font-weight: 300;
    line-height: 52px; color: var(--accent); letter-spacing: -0.5px;
  }
  .intro-text { position: absolute; left: 124px; top: 283px; width: 300px; font-size: 14px; line-height: 26.5px; color: var(--text-light); }

  /* Featured app */
  .client-label { position: absolute; left: 500px; top: 176px; font-size: 14px; color: var(--client-red); }
  .app-name { position: absolute; left: 500px; top: 198px; font-size: 18px; color: #fff; }
  .app-tab-rule { position: absolute; left: 500px; top: 227px; width: 151px; height: 4px; background: var(--accent); }
  .feature-panel { position: absolute; left: 491px; top: 231px; width: 581px; height: 336px; background: var(--panel); }
  .feature-image {
    position: absolute; left: 12px; top: 13px; width: 288px; height: 242px;
    border: 1px solid #bbb; background: linear-gradient(135deg, #fafafa, #dcdcdc);
  }
  .feature-copy { position: absolute; left: 315px; top: 37px; width: 245px; font-size: 13px; line-height: 22px; color: var(--text-body); }
  .feature-copy p + p { margin-top: 22px; }
  .more-link { position: absolute; left: 317px; top: 224px; font-size: 14px; font-weight: 500; color: var(--accent-dark); display: flex; align-items: center; gap: 9px; }
  .action-row { position: absolute; left: 49px; top: 281px; display: flex; }
  .action-btn {
    height: 30px; border-radius: 3px; border: 1px solid #1c86c8;
    background: linear-gradient(#5cc6fb, #2aa0e6); color: #fff; font-size: 16px;
    display: flex; align-items: center; justify-content: center;
    box-shadow: inset 0 1px 0 rgba(255,255,255,0.35);
  }
  .slider-arrow { position: absolute; }

  /* Thumbnail strip */
  .thumb-strip { position: absolute; left: 90px; top: 716px; width: 999px; height: 50px; background: var(--strip); }
  .thumb { position: absolute; top: 649px; width: 88px; height: 92px; }
  .thumb::after { content: ""; position: absolute; left: 0; bottom: -4px; width: 100%; height: 4px; background: var(--accent-dark); }
  .thumb-active { position: absolute; left: 139px; top: 616px; width: 92px; height: 128px; }
  .thumb-active .thumb-fill { width: 92px; height: 92px; background: linear-gradient(135deg, #ffffff, #d6d6d6); }
  .thumb-caption {
    position: absolute; left: 0; top: 92px; width: 92px; height: 36px; background: var(--accent-dark);
    font-size: 12px; color: #fff; text-align: center; padding-top: 8px;
  }
  .thumb-caption::before {
    content: ""; position: absolute; left: 6px; top: -8px;
    border-left: 6px solid transparent; border-right: 6px solid transparent; border-bottom: 8px solid var(--accent-dark);
  }

  /* Footer */
  .site-footer { position: absolute; left: 0; top: 790px; width: 1200px; height: 50px; background: var(--footer); border-top: 1px solid #2e2e2e; }
  .footer-links { position: absolute; left: 143px; top: 16px; display: flex; gap: 25px; font-size: 12px; }
  .footer-links a { color: var(--accent); text-decoration: none; }
  .copyright { position: absolute; left: 755px; top: 16px; font-size: 12px; color: #fff; }
</style>
</head>
<body>

<header class="site-header">
  <div class="brand">
    <span class="brand-dot"></span>
    <span class="brand-name">Stratus Apps</span>
  </div>
  <nav class="main-nav">
    <a href="#" class="is-current">Home</a><span class="sep">/</span>
    <a href="#">Products</a><span class="sep">/</span>
    <a href="#">Buy Now</a><span class="sep">/</span>
    <a href="#">Support</a><span class="sep">/</span>
    <a href="#">About Us</a>
  </nav>
</header>
<div class="header-rule"></div>
<div class="account-menu">Log in or Register
  <svg width="10" height="8" viewBox="0 0 10 8"><path d="M0 0h10L5 8z" fill="#fff"/></svg>
</div>

<h1 class="intro-title">One Platform<br>Many Ideas</h1>
<p class="intro-text">We’re a small Cloud based application studio, based in London. We build state-of-the art, robust applications for structure engineers. They are used for designing buildings, bridges and wharves etc.</p>

<div class="client-label">Client Name</div>
<div class="app-name">Structure App</div>
<div class="app-tab-rule"></div>

<svg class="slider-arrow" style="left:462px;top:391px" width="16" height="32" viewBox="0 0 16 32"><path d="M15 1L2 16l13 15" fill="none" stroke="#4ab2ee" stroke-width="2"/></svg>
<svg class="slider-arrow" style="left:1079px;top:391px" width="16" height="32" viewBox="0 0 16 32"><path d="M1 1l13 15L1 31" fill="none" stroke="#4ab2ee" stroke-width="2"/></svg>

<section class="feature-panel">
  <div class="feature-image" role="img" aria-label="Wireframe rendering of a building with an arched roof"></div>
  <div class="feature-copy">
    <p>Lorem ipsum dolor sit amet, consectetur adipiscing elit. Suspendisse sodales ullamcorper aliquet. Nam porta lobortis inum. Integer sed nibh lacus.</p>
    <p>Nam porta lobortis interdum. Inter sed nibh lacus nter sed nibh lacus nter sed nibh lacus nter sed nibh lacus.</p>
  </div>
  <a class="more-link">More Details
    <svg width="7" height="9" viewBox="0 0 7 9"><path d="M0 0l7 4.5L0 9z" fill="#1f8fd6"/></svg>
  </a>
  <div class="action-row">
    <span class="action-btn" style="width:108px">Free Trial</span>
    <span class="action-btn" style="width:108px;margin-left:14px">Buy It Now</span>
    <span class="action-btn" style="width:120px;margin-left:21px">Screenshots</span>
    <span class="action-btn" style="width:90px;margin-left:17px">Launch</span>
  </div>
</section>

<div class="thumb-strip"></div>
<svg class="slider-arrow" style="left:104px;top:725px" width="16" height="32" viewBox="0 0 16 32"><path d="M15 1L2 16l13 15" fill="none" stroke="#4ab2ee" stroke-width="2"/></svg>
<svg class="slider-arrow" style="left:1057px;top:725px" width="16" height="32" viewBox="0 0 16 32"><path d="M1 1l13 15L1 31" fill="none" stroke="#4ab2ee" stroke-width="2"/></svg>

<div class="thumb-active">
  <div class="thumb-fill" role="img" aria-label="Wireframe building thumbnail"></div>
  <div class="thumb-caption">Structure App</div>
</div>
<div class="thumb" style="left:253px;background:linear-gradient(135deg,#5a2a1a,#c2784a 55%,#3a1c12)" role="img" aria-label="Warm-lit building interior"></div>
<div class="thumb" style="left:369px;background:linear-gradient(135deg,#e8e6d8,#9fb0a6 60%,#dcd8c4)" role="img" aria-label="Glass facade seen from below"></div>
<div class="thumb" style="left:485px;background:linear-gradient(135deg,#dcdcdc,#6e6e6e 55%,#b4b4b4)" role="img" aria-label="Black and white building with trees"></div>
<div class="thumb" style="left:604px;background:linear-gradient(135deg,#1e5a8e,#9fd2ee 50%,#2a6c9a)" role="img" aria-label="Glass tower against sunlit sky"></div>
<div class="thumb" style="left:720px;background:linear-gradient(#cfd3d6,#6a7076 55%,#2c3034)" role="img" aria-label="City skyline and highway"></div>
<div class="thumb" style="left:836px;background:linear-gradient(135deg,#bfe6f6,#3a9ccc 60%,#0e4a6e)" role="img" aria-label="Blue glass corridor"></div>
<div class="thumb" style="left:952px;background:linear-gradient(#7fb0dc,#a96a4e 55%,#8a8a80)" role="img" aria-label="Brick office building"></div>

<footer class="site-footer">
  <nav class="footer-links">
    <a href="#">Contact Us</a>
    <a href="#">Privacy</a>
    <a href="#">Terms of Use</a>
  </nav>
  <p class="copyright">Copyright 2011 Stratus Apps. All Rights Reserved.</p>
</footer>

</body>
</html>
```